Book Cover Design Project For New Nonfiction book

I need a cover designed for a new book/eBook - Little Savers Handbook for Trimming Your Household’s Waste Trail by Moira Fenwick.
Below is a description of the book. I don't have a specific idea or vision in mind for the cover. I'd like to see what designs and ideas ArtHuddle designers come up with.
However, the design needs to work and be effective at both a large book cover size and a small thumbnail-sized image - the way that many people browse book covers on Bookvane and other websites. Therefore, a design that relies on really small details probably won't translate at the smaller image sizes that book covers are displayed online. Just keep that in mind!
Little Savers Handbook for Trimming Your Household’s Waste Trail by Moira Fenwick will help you and your family make your way of life greener: by wasting less, reusing and recycling more. Step-by-step, Moira Fenwick will show you how you can:
• LIVE a much greener lifestyle without sacrificing much in the way of convenience or time
• HARNESS your children’s natural concern about people and the planet
• EMPOWER your children by helping them improve the world
• SAVE your family gobs of money!
• TRACK your progress with a table at the back of the book, to see how much electricity, water, heat, and cash you save!
Following even just a few of the 102 tips in this ebook can have a big impact on your family's economic savings - and the planet!
Target Market(s)
The book is designed to be read by parents and child
Industry/Entity Type
Recycling
Look and feel

```html
<!DOCTYPE html>
<html lang="en">
<head>
<meta charset="utf-8">
<title>Little Savers Handbook – Book Cover</title>
<link rel="stylesheet" href="https://fonts.googleapis.com/css2?family=Arimo:wght@700&family=Tinos:wght@700&display=swap">
<style>
  :root {
    --page: #ffffff;
    --sky-top: #2f7fd0;
    --sky-mid: #7fb6e6;
    --sky-haze: #dfeaf2;
    --hill: #4f7f3a;
    --field: #7fae3c;
    --field-deep: #5a8d2a;
    --skin: #e9b59a;
    --title-red: #e3141b;
    --author-red: #c8151b;
    --ink: #0b0b0b;
    --burst: #fff21f;
    --band: #ffe81a;
  }
  * { margin: 0; padding: 0; box-sizing: border-box; }
  html, body {
    width: 1200px; height: 900px; overflow: hidden;
    background: var(--page);
  }
  .canvas { position: relative; width: 1200px; height: 900px; }
  .cover {
    position: absolute; left: 280px; top: 20px;
    width: 640px; height: 860px; overflow: hidden;
  }
  .cover-scene {
    position: absolute; inset: 0;
    background:
      radial-gradient(ellipse 300px 220px at 330px 690px, var(--skin) 0%, rgba(233,181,154,0.85) 45%, rgba(233,181,154,0) 100%),
      linear-gradient(180deg,
        var(--sky-top) 0%, var(--sky-mid) 28%, var(--sky-haze) 46%,
        var(--hill) 52%, var(--field) 58%, var(--field-deep) 100%);
  }
  .tips-band {
    position: absolute; left: 110px; right: 0; top: 36px; height: 38px;
    background: var(--band);
    display: flex; align-items: center; justify-content: center;
    padding-left: 30px;
    font-family: "Arimo", Arial, sans-serif; font-weight: 700;
    font-size: 27px; color: var(--ink); white-space: nowrap;
  }
  .tips-burst {
    position: absolute; left: -8px; top: 4px; width: 150px; height: 150px;
  }
  .tips-count {
    position: absolute; left: -8px; top: 4px; width: 150px; height: 150px;
    display: flex; flex-direction: column; align-items: center; justify-content: center;
    font-family: "Arimo", Arial, sans-serif; font-weight: 700;
    color: var(--title-red); line-height: 1;
  }
  .tips-count .number { font-size: 48px; }
  .tips-count .label { font-size: 34px; margin-top: 2px; }
  .title {
    position: absolute; left: 80px; right: 0; top: 158px;
    text-align: center;
    font-family: "Tinos", "Times New Roman", serif; font-weight: 700;
    color: var(--title-red); font-size: 90px; line-height: 88px;
  }
  .subtitle {
    position: absolute; left: 110px; right: 20px; top: 348px;
    font-family: "Arimo", Arial, sans-serif; font-weight: 700; color: var(--ink);
  }
  .subtitle .lead { display: block; font-size: 46px; line-height: 54px; text-align: center; }
  .subtitle .rest { display: block; font-size: 31px; line-height: 38px; padding-left: 0; }
  .author {
    position: absolute; left: 0; right: 0; bottom: 36px;
    text-align: center;
    font-family: "Tinos", "Times New Roman", serif; font-weight: 700;
    color: var(--author-red); font-size: 52px;
  }
</style>
</head>
<body>
<main class="canvas">
  <section class="cover">
    <div class="cover-scene" role="img" aria-label="Photo of a green field under a blue sky, with several pairs of cupped family hands holding coins and a small green seedling"></div>

    <div class="tips-band">to a Greener Plant and Pocketbook</div>

    <svg class="tips-burst" viewBox="0 0 150 150" aria-hidden="true">
      <polygon fill="var(--burst)" points="149,75 133,90.5 139,112 117.4,117.4 112,139 90.5,133 75,149 59.5,133 38,139 32.6,117.4 11,112 17,90.5 1,75 17,59.5 11,38 32.6,32.6 38,11 59.5,17 75,1 90.5,17 112,11 117.4,32.6 139,38 133,59.5"/>
    </svg>
    <div class="tips-count"><span class="number">102</span><span class="label">Tips</span></div>

    <h1 class="title">Little Savers</h1>

    <p class="subtitle">
      <span class="lead">Handbook for Trimming</span>
      <span class="rest">Your Household’s Waste Trail</span>
    </p>

    <p class="author">Moira Fenwick</p>
  </section>
</main>
</body>
</html>
```